Professional PowerPoint Template for Data Reports, Presentations

We are a small leadership coaching/consulting firm and would like to update our PowerPoint template that we use with our clients, who are typically mid-senior level company professionals. I've attached a sample Powerpoint as well as our branding guide. The cover page is what needs the most work - just doesn't look current/professional enough. We do want to keep the pages after that clean, with come color but enough space for text and graphics.
Target Market(s)
Senior mgmt and HR executives in small-mid sized companies
Font styles to use
Sans Serif
Requirements
Must have
- Professional
- Clean
- Tied to company color scheme/logo
Nice to have
- Our title pages don't usually have many words on them; we'd like a design that has a lot of color - probably still using mainly our blue but accented with other colors.
- Need simple but smart looking pages after cover with lot of space; mostly we have text on the slides. Currently this is often in bullet point style, but we could probably upgrade the options there.
Should not have
- Anything that looks like a marketing style, as we typically use these with our current clients to share results of data collected, project plans, etc.

```html
<!DOCTYPE html>
<html lang="en">
<head>
<meta charset="utf-8">
<title>Report Cover</title>
<link rel="stylesheet" href="https://fonts.googleapis.com/css2?family=Source+Sans+3:wght@300;400;600&display=swap">
<style>
  :root {
    --brand-blue: #02364c;
    --charcoal: #1f2020;
    --corner-dark: #232323;
    --paper: #ffffff;
    --ink-on-dark: #ffffff;
    --ink-muted: #15191b;
  }
  html, body {
    margin: 0;
    padding: 0;
    width: 792px;
    height: 1200px;
    overflow: hidden;
    background: var(--paper);
  }
  .cover {
    position: relative;
    width: 792px;
    height: 1200px;
    overflow: hidden;
    background: var(--paper);
    font-family: "Source Sans 3", "Myriad Pro", Arial, sans-serif;
  }
  .cover-shapes {
    position: absolute;
    inset: 0;
    width: 792px;
    height: 1200px;
  }
  .shape-charcoal { fill: var(--charcoal); }
  .shape-blue { fill: var(--brand-blue); }
  .shape-corner { fill: var(--corner-dark); }

  .cover-field {
    position: absolute;
    left: 26px;
    margin: 0;
    color: var(--ink-on-dark);
    font-weight: 400;
    line-height: 1;
  }
  .cover-title { top: 177px; font-size: 40px; }
  .cover-date { top: 244px; font-size: 41px; }

  .cover-confidential {
    position: absolute;
    left: 24px;
    top: 382px;
    margin: 0;
    color: var(--ink-muted);
    font-weight: 300;
    font-size: 24px;
    line-height: 1;
    letter-spacing: 0.4px;
  }

  .brand-name {
    position: absolute;
    margin: 0;
    color: var(--ink-on-dark);
    font-weight: 600;
    line-height: 1;
  }
  .brand-name--top { left: 664px; top: 553px; font-size: 26px; }
  .brand-name--bottom { left: 684px; top: 1161px; font-size: 23px; }
</style>
</head>
<body>
  <main class="cover">
    <svg class="cover-shapes" viewBox="0 0 758 1148" preserveAspectRatio="none" aria-hidden="true">
      <polygon class="shape-charcoal" points="468,0 758,285 468,572 0,406 0,166"/>
      <polygon class="shape-blue" points="0,52 588,287 0,519"/>
      <polygon class="shape-corner" points="655,465 758,524 758,573 545,573"/>
      <polygon class="shape-corner" points="670,1057 758,1105 758,1148 576,1148"/>
    </svg>

    <h1 class="cover-field cover-title">Title :</h1>
    <p class="cover-field cover-date">Date:</p>
    <p class="cover-confidential">CONFIDENTIAL</p>

    <p class="brand-name brand-name--top">Halwyn</p>
    <p class="brand-name brand-name--bottom">Halwyn</p>
  </main>
</body>
</html>
```